Women's Health Company needs business card

We need a business card for a USA based women's health care company. We use digital technology to enhance therapy prescribed by clinicians for their patients

```html
<!DOCTYPE html>
<html lang="en">
<head>
<meta charset="UTF-8">
<title>Lunara Health Business Card</title>
<link rel="stylesheet" href="https://fonts.googleapis.com/css2?family=Mulish:wght@700&family=Questrial&display=swap">
<style>
  :root {
    --bg: #e4e4e6;
    --teal: #6dbcb6;
    --purple: #8c56a4;
    --ink: #2b2b2b;
    --white: #ffffff;
    --grad-top: #8a58a2;
    --grad-mid: #8080ac;
    --grad-bottom: #74c1bb;
  }
  * { margin: 0; padding: 0; box-sizing: border-box; }
  html, body {
    width: 1200px; height: 900px; overflow: hidden;
    background: var(--bg);
    font-family: "Questrial", sans-serif;
  }
  .canvas { position: relative; width: 1200px; height: 900px; }
  .card {
    position: absolute; top: 217px; width: 309px; height: 500px;
    box-shadow: 2px 3px 6px rgba(0,0,0,0.35);
  }
  .card-front {
    left: 279px;
    border-radius: 0 60px 0 60px;
    background: linear-gradient(215deg, var(--grad-top) 0%, var(--grad-mid) 50%, var(--grad-bottom) 100%);
  }
  .card-back {
    left: 617px;
    border-radius: 60px 0 60px 0;
    background: var(--white);
  }
  .brand {
    position: absolute; left: 0; right: 0;
    display: flex; align-items: center; justify-content: center; gap: 8px;
    font-family: "Questrial", sans-serif;
    font-size: 30px; letter-spacing: 0.5px; white-space: nowrap;
  }
  .brand-dot { width: 9px; height: 9px; border-radius: 50%; background: var(--purple); }
  .card-front .brand { top: 378px; color: var(--white); }
  .card-front .brand-dot { background: var(--white); }
  .card-back .brand { top: 128px; color: var(--teal); }
  .contact-block { position: absolute; left: 32px; top: 307px; }
  .person-name {
    font-family: "Mulish", sans-serif; font-weight: 700;
    font-size: 21px; color: var(--teal); line-height: 1.1;
  }
  .person-role { font-size: 14px; color: var(--purple); margin-top: 1px; }
  .contact-list { list-style: none; margin-top: 14px; }
  .contact-list li {
    display: flex; align-items: center; gap: 4px;
    font-size: 15px; color: var(--ink); height: 18px;
  }
  .contact-icon { width: 17px; height: 17px; flex: none; }
  .address { margin-top: 14px; font-size: 15px; color: var(--ink); line-height: 18px; }
</style>
</head>
<body>
<main class="canvas">
  <section class="card card-front" aria-label="Card front">
    <div class="brand"><span class="brand-dot"></span>Lunara Health</div>
  </section>

  <section class="card card-back" aria-label="Card back">
    <div class="brand"><span class="brand-dot"></span>Lunara Health</div>
    <div class="contact-block">
      <p class="person-name">Daniel Brooks</p>
      <p class="person-role">Managing Director</p>
      <ul class="contact-list">
        <li>
          <svg class="contact-icon" viewBox="0 0 20 20" aria-hidden="true">
            <circle cx="10" cy="10" r="10" fill="var(--purple)"/>
            <path d="M6.5 5.2l2 .1.8 2.4-1.2 1a7 7 0 0 0 3.2 3.2l1-1.2 2.4.8.1 2c-.1.8-.8 1.3-1.6 1.2C9.6 14.3 5.7 10.4 5.3 6.8c-.1-.8.4-1.5 1.2-1.6z" fill="var(--white)"/>
          </svg>
          044-555 018 246
        </li>
        <li>
          <svg class="contact-icon" viewBox="0 0 20 20" aria-hidden="true">
            <circle cx="10" cy="10" r="10" fill="var(--purple)"/>
            <rect x="4.5" y="6" width="11" height="8" rx="1" fill="var(--white)"/>
            <path d="M4.8 6.5L10 10.8l5.2-4.3" fill="none" stroke="var(--purple)" stroke-width="1.2"/>
          </svg>
          hello@lunarahealth.com
        </li>
        <li>
          <svg class="contact-icon" viewBox="0 0 20 20" aria-hidden="true">
            <circle cx="10" cy="10" r="10" fill="var(--purple)"/>
            <g fill="none" stroke="var(--white)" stroke-width="1.1">
              <circle cx="10" cy="10" r="5.5"/>
              <ellipse cx="10" cy="10" rx="2.4" ry="5.5"/>
              <path d="M4.5 10h11M5.3 7.2h9.4M5.3 12.8h9.4"/>
            </g>
          </svg>
          www.lunarahealth.com
        </li>
      </ul>
      <p class="address">318, Willow Park Avenue<br>60718, Eastland</p>
    </div>
  </section>
</main>
</body>
</html>
```